Business card, envelope and stationary for attorney / law firm
Law firm: Business card, envelope and stationary
Business card, envelope and stationary for attorney / law firm -
Creative Brief
Professional
Morton L. Viskell
Attorney at Law
4718 Brindlewood Court, Suite 300 Larkspur Hollow, CA 96473
mlviskell@viskellpatentfirm.example
WWW.VISKELLPATENTFIRM.EXAMPLE

```html
<!DOCTYPE html>
<html lang="en">
<head>
<meta charset="utf-8">
<title>Viskell Patent Firm – Stationery Set</title>
<link href="https://fonts.googleapis.com/css2?family=Arimo:wght@400;700&display=swap" rel="stylesheet">
<style>
  :root{
    --brand-red:#8a1f22;
    --ink-grey:#7a7a7a;
    --ink-light:#a3a3a3;
    --paper:#ffffff;
    --edge:#d6d6d6;
    --stage:#ffffff;
    --faint-red:rgba(138,31,34,0.07);
  }
  *{margin:0;padding:0;box-sizing:border-box}
  html,body{width:1200px;height:874px;overflow:hidden;background:var(--stage)}
  body{position:relative;font-family:"Arimo",Arial,sans-serif;color:var(--ink-grey)}

  .sheet{position:absolute;background:var(--paper);border:1px solid var(--edge);box-shadow:0 1px 4px rgba(0,0,0,0.08)}

  .brand{position:absolute;display:flex;align-items:center;gap:12px}
  .brand-square{flex:none;background:var(--brand-red)}
  .brand-name{font-weight:700;color:var(--brand-red);letter-spacing:2px;text-transform:uppercase;line-height:1.15;white-space:nowrap}

  /* Letterhead */
  .letterhead{left:43px;top:12px;width:617px;height:828px}
  .letterhead .brand{left:28px;top:60px}
  .letterhead .brand-square{width:52px;height:52px}
  .letterhead .brand-name{font-size:18px}
  .letterhead-address{position:absolute;right:24px;top:30px;text-align:right;font-style:normal;font-size:10.5px;line-height:15px;color:var(--ink-grey)}
  .letterhead-mark{position:absolute;left:209px;width:204px;top:588px;text-align:center;font-weight:700;font-size:40px;letter-spacing:2px;color:var(--faint-red)}
  .letterhead-web{position:absolute;left:0;right:0;bottom:24px;text-align:center;font-size:13px;letter-spacing:3px;color:var(--ink-grey)}

  /* Business card */
  .business-card{left:708px;top:276px;width:252px;height:144px}
  .card-name{position:absolute;left:12px;top:22px;font-size:9px;color:var(--brand-red)}
  .card-title{position:absolute;left:12px;top:34px;font-size:6px;color:var(--ink-light)}
  .card-col{position:absolute;top:20px;font-size:5.5px;line-height:8px;color:var(--ink-grey);padding-left:6px;border-left:1px solid var(--edge);white-space:nowrap}
  .card-col.address{left:100px}
  .card-col.phones{left:176px}
  .business-card .brand{left:28px;top:70px;gap:7px}
  .business-card .brand-square{width:22px;height:22px}
  .business-card .brand-name{font-size:9px;letter-spacing:1px}
  .card-foot{position:absolute;left:0;right:0;bottom:10px;text-align:center;font-size:5px;color:var(--ink-light)}

  /* Envelope */
  .envelope{left:468px;top:456px;width:696px;height:307px}
  .envelope .brand{left:24px;top:36px}
  .envelope .brand-square{width:48px;height:48px}
  .envelope .brand-name{font-size:18px}
  .envelope-address{position:absolute;left:86px;top:98px;font-style:normal;font-size:10px;line-height:14px;color:var(--ink-grey)}
</style>
</head>
<body>

<section class="sheet letterhead" aria-label="Letterhead">
  <div class="brand">
    <span class="brand-square"></span>
    <span class="brand-name">Viskell<br>Patent Firm</span>
  </div>
  <address class="letterhead-address">
    4718 Brindlewood Court<br>
    Suite 300<br>
    Larkspur Hollow, CA 96473<br>
    Ph: 530.555.0142<br>
    Fax: 530.555.0187
  </address>
  <div class="letterhead-mark">VISKELL</div>
  <div class="letterhead-web">WWW.VISKELLPATENTFIRM.EXAMPLE</div>
</section>

<section class="sheet business-card" aria-label="Business card">
  <div class="card-name">Morton L. Viskell</div>
  <div class="card-title">Attorney at Law</div>
  <div class="card-col address">4718 Brindlewood Ct.<br>Suite 300<br>Larkspur Hollow, CA 96473</div>
  <div class="card-col phones">Ph: 530.555.0142<br>Cell: 530.555.0163<br>Fax: 530.555.0187</div>
  <div class="brand">
    <span class="brand-square"></span>
    <span class="brand-name">Viskell<br>Patent Firm</span>
  </div>
  <div class="card-foot">mlviskell@viskellpatentfirm.example &nbsp;|&nbsp; WWW.VISKELLPATENTFIRM.EXAMPLE</div>
</section>

<section class="sheet envelope" aria-label="Envelope">
  <div class="brand">
    <span class="brand-square"></span>
    <span class="brand-name">Viskell<br>Patent Firm</span>
  </div>
  <address class="envelope-address">
    4718 Brindlewood Court, Suite 300<br>
    Larkspur Hollow, CA 96473
  </address>
</section>

</body>
</html>
```